General pharmacy flyer for a pharmacy. see attached files for similar flyer design
picture should be of a black person/pharmacist
Services available
Repeat Prescription collection
Emergency Contraception
Contraceptive pill
Vitamins
and more.....
Industry/Entity Type
Pharmacy

```html
<!DOCTYPE html>
<html lang="en">
<head>
<meta charset="utf-8">
<title>Halo Pharmacy Flyer</title>
<link href="https://fonts.googleapis.com/css2?family=Oswald:wght@400;500;700&family=Roboto:wght@400;500;700&display=swap" rel="stylesheet">
<style>
  :root {
    --blue: #1f8fd6;
    --blue-dark: #0c6db4;
    --blue-light: #bfe3f8;
    --green: #8cc63f;
    --green-dark: #5ea62a;
    --red: #e5262b;
    --yellow: #ffe36a;
    --white: #ffffff;
    --ink: #1d2a36;
    --paper: #eef1f4;
  }
  html, body { margin: 0; padding: 0; overflow: hidden; background: var(--paper); }
  .flyer {
    position: relative; width: 870px; height: 1200px; overflow: hidden;
    background: var(--white); font-family: 'Roboto', sans-serif; color: var(--ink);
  }
  .brand { position: absolute; left: 40px; top: 34px; z-index: 3; }
  .brand-name {
    font-family: 'Oswald', sans-serif; font-weight: 700; font-size: 92px;
    line-height: 1; color: var(--blue); letter-spacing: 1px; display: flex; align-items: center; gap: 16px;
  }
  .brand-dot { width: 30px; height: 30px; border-radius: 50%; background: var(--green); }
  .tagline {
    font-family: 'Oswald', sans-serif; font-weight: 500; font-size: 27px;
    color: var(--red); margin-top: 8px; letter-spacing: 0.5px;
  }
  .hours { position: absolute; left: 270px; top: 160px; width: 210px; height: 210px; z-index: 3; }
  .hours svg { position: absolute; inset: 0; width: 100%; height: 100%; }
  .hours-text {
    position: absolute; inset: 0; display: flex; flex-direction: column;
    align-items: center; justify-content: center; text-align: center;
    font-family: 'Oswald', sans-serif; color: var(--white); font-size: 18px; line-height: 1.15;
  }
  .hours-text .open { font-size: 21px; font-weight: 700; transform: rotate(-8deg); margin-bottom: 3px; }
  .hours-text .time { color: var(--yellow); font-weight: 700; }
  .hours-text .sep { font-size: 12px; line-height: 1; }
  .contact { position: absolute; right: 40px; top: 165px; text-align: right; z-index: 3; }
  .contact-icon { display: block; margin-left: auto; margin-bottom: 4px; }
  .phone {
    font-family: 'Oswald', sans-serif; font-weight: 700; font-size: 58px;
    color: var(--green-dark); line-height: 1.05;
  }
  .email { font-size: 15px; color: var(--ink); letter-spacing: 0.5px; margin-top: 6px; text-transform: uppercase; }
  .photo {
    position: absolute; left: 0; top: 380px; width: 870px; height: 620px;
    background: linear-gradient(120deg, #dfe9ee 0%, #9fbccc 35%, #5f7d55 55%, #c8d3c2 80%, #e9eef0 100%);
  }
  .waves { position: absolute; left: 0; top: 350px; width: 870px; height: 700px; z-index: 1; }
  .services {
    position: absolute; left: 520px; top: 810px; width: 320px; height: 215px; z-index: 2;
    background: var(--white); border-radius: 14px; padding: 20px 24px; box-sizing: border-box;
    box-shadow: 0 4px 14px rgba(0,0,0,0.15);
  }
  .services h2 { margin: 0 0 10px; font-size: 24px; font-weight: 700; color: var(--ink); }
  .services ul { list-style: none; margin: 0; padding: 0; }
  .services li { font-size: 18px; line-height: 1.45; display: flex; align-items: center; gap: 10px; }
  .tick { flex: none; }
  .footer {
    position: absolute; left: 0; top: 1045px; width: 870px; height: 155px; background: var(--green); z-index: 2;
  }
  .stores { position: absolute; left: 40px; top: 18px; color: var(--white); }
  .stores h3 { margin: 0 0 10px; font-size: 27px; font-weight: 700; }
  .stores p { margin: 6px 0; font-size: 17px; display: flex; align-items: center; gap: 10px; }
  .care {
    position: absolute; right: 0; top: 0; width: 250px; height: 155px; background: var(--blue);
    clip-path: polygon(14% 0, 100% 0, 100% 100%, 0 100%);
    color: var(--white); font-family: 'Oswald', sans-serif; text-align: center;
    display: flex; flex-direction: column; justify-content: center; padding-left: 30px; box-sizing: border-box;
  }
  .care .small { font-size: 25px; font-weight: 500; line-height: 1.1; }
  .care .big { font-size: 42px; font-weight: 700; line-height: 1.1; }
</style>
</head>
<body>
<main class="flyer">
  <header class="brand">
    <div class="brand-name">HALO PHARMACY <span class="brand-dot"></span></div>
    <div class="tagline">FOR ALL YOUR PRESCRIPTION NEEDS AND MORE</div>
  </header>

  <div class="hours">
    <svg viewBox="0 0 200 200" aria-hidden="true">
      <polygon fill="#e5262b" points="100,0 111,21 130,5 135,28 158,19 154,42 178,41 166,62 190,70 170,84 192,100 170,116 190,130 166,138 178,159 154,158 158,181 135,172 130,195 111,179 100,200 89,179 70,195 65,172 42,181 46,158 22,159 34,138 10,130 30,116 8,100 30,84 10,70 34,62 22,41 46,42 42,19 65,28 70,5 89,21"/>
    </svg>
    <div class="hours-text">
      <span class="open">OPEN</span>
      <span>MON - FRI</span>
      <span class="time">9AM - 6PM</span>
      <span class="sep">•</span>
      <span>SATURDAY</span>
      <span class="time">10AM - 5PM</span>
    </div>
  </div>

  <div class="contact">
    <svg class="contact-icon" width="34" height="30" viewBox="0 0 34 30" aria-hidden="true">
      <path fill="#1d2a36" d="M2 8c0-4 7-7 15-7s15 3 15 7v3h-8V8H10v3H2z"/>
      <rect x="6" y="13" width="22" height="15" rx="3" fill="#1d2a36"/>
      <circle cx="17" cy="20.5" r="4" fill="#fff"/>
    </svg>
    <div class="phone">482 3051</div>
    <div class="phone">482 3058</div>
    <div class="email">halopharmacy@mail.com</div>
  </div>

  <div class="photo" role="img" aria-label="Smiling pharmacist in a green shirt holding out a medicine bottle in front of pharmacy shelves, with a customer on the right"></div>

  <svg class="waves" viewBox="0 0 870 700" preserveAspectRatio="none" aria-hidden="true">
    <path fill="#ffffff" d="M0 0 H870 V20 C620 70 300 0 0 50 Z"/>
    <path fill="#1f8fd6" d="M0 50 C300 0 620 70 870 20 V38 C620 90 300 20 0 72 Z"/>
    <path fill="#bfe3f8" d="M0 540 C250 450 520 540 870 410 V700 H0 Z"/>
    <path fill="#1f8fd6" d="M0 570 C260 480 540 570 870 450 V700 H0 Z"/>
    <path fill="#0c6db4" d="M0 630 C300 560 560 630 870 540 V700 H0 Z"/>
  </svg>

  <section class="services">
    <h2>Services include</h2>
    <ul>
      <li><svg class="tick" width="16" height="14" viewBox="0 0 16 14"><path d="M1 7l5 5L15 1" stroke="#1d2a36" stroke-width="2.6" fill="none"/></svg>Repeat prescription collection</li>
      <li><svg class="tick" width="16" height="14" viewBox="0 0 16 14"><path d="M1 7l5 5L15 1" stroke="#1d2a36" stroke-width="2.6" fill="none"/></svg>Emergency contraception</li>
      <li><svg class="tick" width="16" height="14" viewBox="0 0 16 14"><path d="M1 7l5 5L15 1" stroke="#1d2a36" stroke-width="2.6" fill="none"/></svg>Contraceptive pill</li>
      <li><svg class="tick" width="16" height="14" viewBox="0 0 16 14"><path d="M1 7l5 5L15 1" stroke="#1d2a36" stroke-width="2.6" fill="none"/></svg>Vitamins</li>
      <li><svg class="tick" width="16" height="14" viewBox="0 0 16 14"><path d="M1 7l5 5L15 1" stroke="#1d2a36" stroke-width="2.6" fill="none"/></svg>And More...</li>
    </ul>
  </section>

  <footer class="footer">
    <div class="stores">
      <h3>2 Stores to serve you better:</h3>
      <p><svg width="16" height="22" viewBox="0 0 16 22"><path fill="#0c6db4" d="M8 0a8 8 0 0 0-8 8c0 6 8 14 8 14s8-8 8-14a8 8 0 0 0-8-8z"/><circle cx="8" cy="8" r="3" fill="#fff"/></svg>42 Orchard Street (Corner of Orchard and Bay Street)</p>
      <p><svg width="16" height="22" viewBox="0 0 16 22"><path fill="#0c6db4" d="M8 0a8 8 0 0 0-8 8c0 6 8 14 8 14s8-8 8-14a8 8 0 0 0-8-8z"/><circle cx="8" cy="8" r="3" fill="#fff"/></svg>Harbour Quay, Westmoor, St Aldan</p>
    </div>
    <div class="care">
      <span class="small">WE CARE</span>
      <span class="small">ABOUT YOUR</span>
      <span class="big">HEALTH</span>
    </div>
  </footer>
</main>
</body>
</html>
```